Calloway needs a modernized design

We would like a modern update (that can be responsive) to our existing website. Attached are the two existing pages we would like new concepts of - our home page and a page about one of our locations.

Calloway is provides executive offices and virtual office services. Startups, law firms, and financial services are our primary clients. We would like a professional, clean design, leaning towards minimalist. We intend to greatly reduce/eliminate the long paragraphs of text.

Industry/Entity Type

Business Service

Number of Pages Required

2 page

Requirements
Must have
• A design that can be responsive
Nice to have
• Large image(s) on home page that rotate.

```html
<!DOCTYPE html>
<html lang="en">
<head>
<meta charset="utf-8">
<title>Calloway Business Centers</title>
<link href="https://fonts.googleapis.com/css2?family=Open+Sans:wght@400;600;700&family=Roboto:wght@300;400;500;700&display=swap" rel="stylesheet">
<style>
:root{
  --navy:#1f2f58;
  --navy-dark:#17233f;
  --blue:#2c5aa9;
  --text:#555b66;
  --muted:#8a909a;
  --light:#eef0f3;
  --white:#ffffff;
  --orange:#f0962a;
  --green:#4caf50;
  --red:#e8562a;
  --purple:#6a3fa0;
  --social:#d9433b;
}
*{box-sizing:border-box;margin:0;padding:0}
html,body{width:791px;height:1200px;overflow:hidden}
body{font-family:"Open Sans",Arial,sans-serif;color:var(--text);background:var(--white);position:relative;font-size:8px;line-height:1.5}
.site-header{height:37px;display:flex;align-items:center;justify-content:space-between;padding:0 70px 0 18px}
.brand{display:flex;align-items:center;gap:5px}
.brand-mark{width:14px;height:14px;background:var(--navy)}
.brand-name{font-family:"Roboto",sans-serif;font-weight:700;font-size:11px;color:var(--navy);letter-spacing:.5px}
.main-nav{display:flex;gap:4px;font-size:8px}
.main-nav a{color:var(--navy);text-decoration:none;padding:5px 9px}
.main-nav a.active{background:var(--navy);color:var(--white)}
.hero{position:absolute;top:37px;left:0;width:791px;height:327px;background:linear-gradient(100deg,#f4f5f6 0%,#dfe3e8 40%,#3b4a66 75%,#6d7a90 100%)}
.hero-card{position:absolute;left:0;top:100px;width:230px;height:150px;background:rgba(255,255,255,.92);padding:24px 20px 0 18px}
.section-num{font-family:"Roboto",sans-serif;font-size:14px;color:var(--navy);font-weight:500}
.section-num sup{font-size:7px}
.hero-card h1{font-family:"Roboto",sans-serif;font-weight:500;font-size:19px;color:var(--navy);line-height:1.2;margin:2px 0 6px}
.hero-card p{font-size:7.5px;color:var(--text)}
.btn{display:inline-block;background:var(--navy);color:var(--white);font-size:7px;padding:5px 10px;text-decoration:none}
.hero-card .btn{margin-top:9px}
.suites{position:absolute;top:394px;left:71px;width:650px;height:150px}
.office-menu{position:absolute;left:0;top:0;width:140px;list-style:none}
.office-menu li{height:18px;margin-bottom:6px;color:var(--white);font-size:7px;padding:4px 8px;display:flex;justify-content:space-between}
.office-menu li:nth-child(1){background:var(--blue)}
.office-menu li:nth-child(2){background:var(--orange)}
.office-menu li:nth-child(3){background:var(--green)}
.office-menu li:nth-child(4){background:var(--red)}
.office-menu li:nth-child(5){background:var(--purple)}
.suites-photo{position:absolute;left:146px;top:0;width:146px;height:138px;background:linear-gradient(135deg,#d9e3ec,#a8b8c7 60%,#e8ecef)}
.suites-text{position:absolute;left:338px;top:0;width:312px}
.suites-text h2,.value-text h2{font-family:"Roboto",sans-serif;font-weight:500;font-size:12px;color:var(--navy);margin:2px 0 4px}
.suites-text h3{font-size:7.5px;font-weight:600;color:var(--navy);margin-bottom:3px}
.suites-text p{font-size:7px;margin-bottom:8px}
.services{position:absolute;top:567px;left:0;width:791px;height:198px;background:var(--light);text-align:center}
.services h2{font-family:"Roboto",sans-serif;font-size:11px;font-weight:500;color:var(--navy);padding-top:18px}
.rule{width:40px;height:2px;background:var(--navy);margin:5px auto 0}
.service-list{display:flex;justify-content:center;gap:50px;margin-top:16px}
.service{width:150px}
.service-icon{width:36px;height:36px;border-radius:50%;background:var(--navy);margin:0 auto 7px;display:flex;align-items:center;justify-content:center}
.service h3{font-size:7.5px;font-weight:700;color:var(--navy);margin-bottom:4px}
.service p{font-size:6.8px}
.value{position:absolute;top:790px;left:0;width:791px;height:200px}
.value-text{position:absolute;left:60px;top:22px;width:413px;text-align:right}
.value-text h2{margin-top:0}
.value-text p{font-size:7px;margin-bottom:12px}
.value-photo{position:absolute;left:493px;top:10px;width:240px;height:135px;background:linear-gradient(160deg,#c8c2b5,#8c7e68 55%,#5b5042)}
.value-caption{position:absolute;left:493px;top:152px;font-size:7px}
.value-caption strong{display:block;color:var(--navy);font-size:8px}
.site-footer{position:absolute;top:1002px;left:0;width:791px;height:178px;background:var(--navy);color:#c7ceda;padding:20px 18px}
.footer-about{position:absolute;left:18px;top:18px;width:180px}
.footer-about .brand-name{color:var(--white)}
.footer-about .brand-mark{background:var(--white)}
.footer-about p{font-size:6.5px;margin-top:8px}
.footer-about a{display:block;margin-top:6px;color:var(--white);font-size:7px;font-weight:600;text-decoration:none}
.footer-links{position:absolute;left:240px;top:18px;width:140px}
.site-footer h4{font-size:8px;color:var(--white);font-weight:600;margin-bottom:7px}
.link-cols{display:flex;gap:22px;list-style:none}
.link-cols ul{list-style:none;font-size:6.5px;line-height:1.9}
.photos{position:absolute;left:395px;top:18px;width:140px}
.photo-grid{display:grid;grid-template-columns:repeat(4,26px);gap:5px}
.photo-grid div{height:22px;background:linear-gradient(135deg,#8da2bd,#4c5f80)}
.newsletter{position:absolute;left:580px;top:18px;width:195px}
.subscribe{display:flex}
.subscribe span{flex:1;background:var(--white);color:var(--muted);font-size:6.5px;padding:5px 6px}
.subscribe b{background:var(--navy-dark);color:var(--white);font-size:6.5px;padding:5px 6px}
.social{display:flex;gap:5px;margin-top:10px}
.social i{width:14px;height:14px;border-radius:50%;background:var(--social)}
.copyright{position:absolute;top:1180px;left:0;width:791px;height:20px;background:var(--navy-dark);color:#9aa4b6;font-size:6.5px;padding:5px 18px}
</style>
</head>
<body>
<header class="site-header">
  <div class="brand"><span class="brand-mark"></span><span class="brand-name">CALLOWAY</span></div>
  <nav class="main-nav">
    <a class="active" href="#">Home</a><a href="#">Properties</a><a href="#">Virtual tours &amp; videos</a><a href="#">Photos</a><a href="#">Broker referrals</a>
  </nav>
</header>

<section class="hero" role="img" aria-label="Photo of a businessman in a suit working at a laptop in a bright office">
  <div class="hero-card">
    <div class="section-num">01<sup>01</sup></div>
    <h1>Executive Office Solutions</h1>
    <p>Come See Why Growing Companies are Choosing Calloway Business Centers for Flexible, Fully Serviced Executive Space</p>
    <a class="btn" href="#">READ MORE</a>
  </div>
</section>

<section class="suites">
  <ul class="office-menu">
    <li>Executive office suites<span>›</span></li>
    <li>Virtual office packages<span>›</span></li>
    <li>Meeting &amp; training rooms<span>›</span></li>
    <li>Coworking memberships<span>›</span></li>
    <li>Video conference rooms<span>›</span></li>
  </ul>
  <div class="suites-photo" role="img" aria-label="Photo of a team meeting around a table with documents"></div>
  <div class="suites-text">
    <div class="section-num">02<sup>02</sup></div>
    <h2>EXECUTIVE OFFICE SUITES</h2>
    <h3>Professional Office Space Solutions. One Low Cost</h3>
    <p>Are you looking for office space in a prime location? Whether you are a growing startup, a law firm or a financial practice, Calloway offers furnished suites with reception, internet, meeting rooms and support staff included. Flexible terms let you move in quickly and scale as your business grows, all for one simple monthly fee with no hidden costs.</p>
    <a class="btn" href="#">See More</a>
  </div>
</section>

<section class="services">
  <h2>OUR SERVICES</h2>
  <div class="rule"></div>
  <div class="service-list">
    <div class="service">
      <div class="service-icon"><svg width="16" height="16" viewBox="0 0 16 16"><path d="M8 1a5 5 0 0 0-5 5c0 4 5 9 5 9s5-5 5-9a5 5 0 0 0-5-5z" fill="#fff"/><circle cx="8" cy="6" r="2" fill="#1f2f58"/></svg></div>
      <h3>LOCATION</h3>
      <p>Lorem ipsum dolor sit amet, consectetur adipiscing elit. Aenean commodo ligula eget dolor massa cum sociis natoque.</p>
    </div>
    <div class="service">
      <div class="service-icon"><svg width="16" height="16" viewBox="0 0 16 16"><rect x="2" y="10" width="8" height="3" fill="#fff"/><rect x="6" y="2" width="4" height="7" transform="rotate(-40 8 6)" fill="#fff"/></svg></div>
      <h3>LAW FIRMS</h3>
      <p>Lorem ipsum dolor sit amet, consectetur adipiscing elit. Aenean commodo ligula eget dolor massa cum sociis natoque.</p>
    </div>
    <div class="service">
      <div class="service-icon"><svg width="16" height="16" viewBox="0 0 16 16"><path d="M8 1 1 5h14z" fill="#fff"/><rect x="3" y="6" width="2" height="6" fill="#fff"/><rect x="7" y="6" width="2" height="6" fill="#fff"/><rect x="11" y="6" width="2" height="6" fill="#fff"/><rect x="1" y="13" width="14" height="2" fill="#fff"/></svg></div>
      <h3>FINANCIAL SERVICES</h3>
      <p>Lorem ipsum dolor sit amet, consectetur adipiscing elit. Aenean commodo ligula eget dolor massa cum sociis natoque.</p>
    </div>
  </div>
</section>

<section class="value">
  <div class="value-text">
    <div class="section-num">03<sup>03</sup></div>
    <h2>Value</h2>
    <p>Either you need Calloway executive suites, virtual offices or meeting rooms, you can find a solution that fits your budget. We provide a polished address, a friendly reception team, mail handling and fast internet, so you can focus on clients. Our members enjoy business lounges and networking events at every center, and flexible agreements that adapt as your company grows.</p>
    <a class="btn" href="#">See More</a>
  </div>
  <div class="value-photo" role="img" aria-label="Photo of a furnished private office with desk and window"></div>
  <div class="value-caption"><strong>Community</strong>Companies that perform</div>
</section>

<footer class="site-footer">
  <div class="footer-about">
    <div class="brand"><span class="brand-mark"></span><span class="brand-name">CALLOWAY</span></div>
    <p>Calloway Business Centers has provided flexible executive suites and virtual office services for years, helping startups, law firms and financial firms work from a prime address.</p>
    <a href="#">Request a Free Quotation</a>
  </div>
  <div class="footer-links">
    <h4>Useful Links</h4>
    <div class="link-cols">
      <ul><li>› About Us</li><li>› Contact Us</li><li>› Home</li><li>› Testimonials</li><li>› FAQ</li><li>› Careers</li></ul>
      <ul><li>› Purchases</li><li>› Specials</li><li>› Site Map</li><li>› Privacy</li></ul>
    </div>
  </div>
  <div class="photos">
    <h4>Property Photos</h4>
    <div class="photo-grid" role="img" aria-label="Thumbnail photos of office buildings">
      <div></div><div></div><div></div><div></div><div></div><div></div><div></div><div></div>
    </div>
  </div>
  <div class="newsletter">
    <h4>Newsletter</h4>
    <div class="subscribe"><span>Email address</span><b>OK</b></div>
    <div class="social"><i></i><i></i><i></i><i></i><i></i><i></i></div>
  </div>
</footer>
<div class="copyright">Copyright 2017 Calloway Business Centers All Rights Reserved</div>
</body>
</html>
```